Business Card & Logo Design for a communications based company

I am looking for a business card and logo design for a communications based company.. We specialize in Fiber Optics
I have an image i would like to use towards the logo which i have uploaded. (Use of the image is totally up to you the designers)
Background color - Blue OR Black. (thats just my preference..Use of those colors are totally up to the designer)
Text -
Company Name - Orbivane Communications LTD
Name - Kelvin Persadsingh
Contact Number - (868) 555-0172
Adress - Harborvale
Company Motto - Stay Connected !
Services Offered
Fiber Optic Solutions
Full Networking Solutions
IP Surveillance Systems
Access Control Systems
Alarms
Communications
Text -
Name - Kelvin Persadsingh
Adress - Harborvale
Services Offered
Fiber Optic Solutions
Full Networking Solutions
IP Surveillance Systems
Access Control Systems
Alarms

```html
<!DOCTYPE html>
<html lang="en">
<head>
<meta charset="utf-8">
<title>Orbivane Communications LTD – Business Cards</title>
<link href="https://fonts.googleapis.com/css2?family=Open+Sans:wght@400;600;700&family=Cinzel:wght@400&display=swap" rel="stylesheet">
<style>
  :root {
    --backdrop: #dcdcdc;
    --card-blue: #0b8ae6;
    --card-white: #f4f4f2;
    --ink: #111111;
    --ink-navy: #0c1f3a;
    --paper-text: #ffffff;
    --shadow: rgba(0,0,0,0.18);
  }
  * { box-sizing: border-box; margin: 0; padding: 0; }
  html, body { width: 1200px; height: 900px; overflow: hidden; }
  body {
    background: var(--backdrop);
    font-family: "Open Sans", Arial, sans-serif;
    position: relative;
  }
  .card {
    position: absolute;
    top: 296px;
    width: 540px;
    height: 309px;
    box-shadow: 0 6px 18px var(--shadow);
    overflow: hidden;
  }
  .card--front { left: 40px; background: var(--card-blue); }
  .card--back { left: 620px; display: flex; }

  .brand { display: flex; align-items: center; gap: 10px; color: var(--ink); }
  .brand__text { display: flex; flex-direction: column; line-height: 1; font-weight: 600; }
  .brand__name { font-size: 46px; letter-spacing: 1px; }
  .brand__sub { font-size: 14px; margin-top: 4px; letter-spacing: 0.3px; }
  .brand__dot { width: 34px; height: 34px; border-radius: 50%; background: var(--ink-navy); flex: none; margin-top: 22px; }

  .card--front .brand { position: absolute; left: 150px; top: 70px; }
  .motto {
    position: absolute; left: 70px; top: 190px;
    font-size: 36px; font-weight: 700; color: var(--paper-text);
  }

  .back__logo-panel {
    width: 40%; background: var(--card-white);
    display: flex; align-items: center; justify-content: center;
  }
  .back__logo-panel .brand__name { font-size: 34px; }
  .back__logo-panel .brand__sub { font-size: 11px; }
  .back__logo-panel .brand__dot { width: 24px; height: 24px; margin-top: 16px; }
  .back__logo-panel .brand { gap: 6px; }

  .back__info { width: 60%; background: var(--card-blue); position: relative; }
  .holder {
    position: absolute; top: 28px; right: 26px;
    font-family: "Cinzel", Georgia, serif; font-size: 15px; letter-spacing: 1.5px;
    color: var(--ink-navy);
  }
  .services {
    position: absolute; top: 86px; left: 0; right: 0;
    list-style: none; text-align: center;
    color: var(--paper-text); font-size: 13px; line-height: 1.35;
  }
  .contact {
    position: absolute; left: 22px; bottom: 24px;
    list-style: none; color: var(--ink); font-size: 17px; font-weight: 600;
  }
  .contact__item { display: flex; align-items: center; gap: 8px; margin-top: 6px; }
  .contact__icon { width: 18px; height: 18px; flex: none; }
</style>
</head>
<body>
  <section class="card card--front" aria-label="Card front">
    <div class="brand">
      <div class="brand__text">
        <span class="brand__name">Orbivane</span>
        <span class="brand__sub">Communications LTD</span>
      </div>
      <span class="brand__dot"></span>
    </div>
    <p class="motto">Stay Connected !</p>
  </section>

  <section class="card card--back" aria-label="Card back">
    <div class="back__logo-panel">
      <div class="brand">
        <div class="brand__text">
          <span class="brand__name">Orbivane</span>
          <span class="brand__sub">Communications LTD</span>
        </div>
        <span class="brand__dot"></span>
      </div>
    </div>
    <div class="back__info">
      <p class="holder">Kelvin Persadsingh</p>
      <ul class="services">
        <li>Fiber Optic Solutions</li>
        <li>Full Networking Solutions</li>
        <li>IP Surveillance Systems</li>
        <li>Access Control Systems</li>
        <li>Alarms</li>
      </ul>
      <ul class="contact">
        <li class="contact__item">
          <svg class="contact__icon" viewBox="0 0 20 20" aria-hidden="true">
            <circle cx="10" cy="10" r="10" fill="#ffffff"/>
            <path d="M7 5.5l1.6 2.2-1 1.2a6 6 0 0 0 3.5 3.5l1.2-1 2.2 1.6-.8 1.6c-4 .2-7.9-3.7-7.7-7.7z" fill="#0b8ae6"/>
          </svg>
          <span>555.555.0172</span>
        </li>
        <li class="contact__item">
          <svg class="contact__icon" viewBox="0 0 20 20" aria-hidden="true">
            <circle cx="10" cy="10" r="10" fill="#ffffff"/>
            <path d="M10 4a4 4 0 0 0-4 4c0 3 4 8 4 8s4-5 4-8a4 4 0 0 0-4-4z" fill="#0b8ae6"/>
            <circle cx="10" cy="8" r="1.5" fill="#ffffff"/>
          </svg>
          <span>Harborvale</span>
        </li>
      </ul>
    </div>
  </section>
</body>
</html>
```